PowerPoint design MedoraVix

We need a PowerPoint set-up based upon our existing logo (see joint file)
Our company is operating in the health care and life science sector. We are mainly focussing on international business

Target Market(s)

International

Industry/Entity Type

health care and life sciences

Requirements
Must have
• Logos as added

```html
<!DOCTYPE html>
<html lang="en">
<head>
<meta charset="utf-8">
<title>MedoraVix Presentation</title>
<link href="https://fonts.googleapis.com/css2?family=Lato:wght@300;400;700;900&family=Arimo:wght@400;700&display=swap" rel="stylesheet">
<style>
:root{
  --canvas:#4a4a4a;
  --green:#46b21b;
  --blue:#0f3a73;
  --blue-mid:#1d4f8a;
  --ink:#2b2b2b;
  --card:#f7f4f4;
  --white:#ffffff;
}
*{box-sizing:border-box;margin:0;padding:0}
html,body{width:1200px;height:3785px;overflow:hidden;background:var(--canvas)}
body{position:relative;font-family:"Arimo",Arial,sans-serif;color:var(--ink)}
.slide{position:absolute;left:107px;width:1002px;height:563px;overflow:hidden}
.brand{position:absolute;left:22px;top:22px;display:flex;align-items:center;gap:12px}
.brand-dot{width:38px;height:38px;border-radius:50%;background:var(--blue-mid)}
.brand-name{font-family:"Lato",sans-serif;font-weight:700;font-size:29px;color:var(--blue-mid)}
.footer-bar{position:absolute;bottom:0;height:6px}
.footer-bar.green{left:0;width:505px;background:var(--green)}
.footer-bar.blue{left:509px;right:0;background:var(--blue)}

/* welcome */
.s-welcome{top:117px;background:radial-gradient(ellipse at 40% 30%,#2b3750 0%,#1a2235 55%,#121827 100%)}
.s-welcome .bg{position:absolute;inset:0}
.s-welcome .title{position:absolute;top:204px;width:100%;text-align:center;font-family:"Lato",sans-serif;font-weight:900;font-size:36px;line-height:44px;color:var(--white)}
.s-welcome .subtitle{position:absolute;top:259px;width:100%;text-align:center;font-family:"Lato",sans-serif;font-weight:300;font-size:29px;line-height:36px;color:var(--white)}
.s-welcome .brand{top:472px;left:30px}
.s-welcome .brand-name{color:#2c5fa0}
.s-welcome .brand-dot{background:#2c5fa0}

/* services */
.s-services{top:729px;background:linear-gradient(180deg,#dcdee2 0%,#eceef0 40%,#c9ccd1 70%,#e9eaec 100%)}
.tab{position:absolute;right:0;top:0;width:270px;height:60px}
.tab-label{position:absolute;right:0;top:0;width:240px;height:60px;display:flex;align-items:center;justify-content:center;font-family:"Lato",sans-serif;font-weight:900;font-size:20px;color:var(--white)}
.card{position:absolute;top:159px;width:232px;height:343px;background:var(--card);text-align:center}
.card-icon{position:absolute;left:73px;top:-35px;width:86px;height:86px}
.card h3{position:absolute;top:75px;width:100%;font-weight:700;font-size:14px;line-height:18px;color:var(--blue)}
.card p{position:absolute;top:112px;left:23px;right:23px;font-size:11.2px;line-height:17.2px;color:var(--ink)}

/* about */
.s-about{top:1340px;background:linear-gradient(160deg,#f3f5f8 0%,#e7ecf1 100%)}
.s-about .visual{position:absolute;inset:0}
.s-about h2{position:absolute;left:37px;top:138px;font-family:"Lato",sans-serif;font-weight:900;font-size:20px;color:var(--blue)}
.s-about .copy{position:absolute;left:37px;top:180px;width:322px;font-size:11.3px;line-height:15.6px;color:var(--ink)}
.s-about .copy p{margin-bottom:14px;text-align:justify}
.s-about .copy p.left{text-align:left}

/* process */
.s-process{top:1952px;background:radial-gradient(ellipse at 55% 35%,#f7f9fc 0%,#e4e9f0 60%,#d6dce5 100%)}
.s-process .bg{position:absolute;inset:0}
.step{position:absolute;width:140px;height:140px;border-radius:50%;background:rgba(255,255,255,.55);box-shadow:0 0 0 1px rgba(140,150,220,.25)}
.step-ring{position:absolute;left:11px;top:11px;width:118px;height:118px;border-radius:50%;background:linear-gradient(135deg,#a9b2ff,#5d66e8)}
.step-face{position:absolute;left:24px;top:22px;width:92px;height:92px;border-radius:50%;background:var(--white);display:flex;align-items:center;justify-content:center;font-family:"Lato",sans-serif;font-weight:900;font-size:44px;color:var(--green)}
.note{position:absolute;width:160px;text-align:center}
.note h4{font-size:11.5px;font-weight:700;color:var(--ink);margin-bottom:5px}
.note p{font-size:9.3px;line-height:11.8px;color:#3a3a3a}
.stem{position:absolute;width:1px;background:rgba(120,140,200,.35)}
.pin{position:absolute;width:5px;height:5px;border-radius:50%;background:#5d66e8}

/* solutions */
.s-solutions{top:2563px;background:linear-gradient(180deg,#ffffff 0%,#f1f1f1 50%,#fbfbfb 100%)}
.s-solutions .head{position:absolute;left:257px;top:22px}
.s-solutions .head h2{font-weight:700;font-size:15.5px;color:var(--blue)}
.s-solutions .head p{font-size:12.3px;color:var(--ink);margin-top:2px}
.photo{position:absolute;top:122px;width:250px;height:250px;border-radius:50%;border:14px solid var(--green)}
.photo.dna{background:radial-gradient(circle at 40% 40%,#d9eaf2,#8fb7cc)}
.photo.care{background:radial-gradient(circle at 50% 55%,#d7263a 0%,#e8dcdc 35%,#f4f2f2 70%)}
.photo.cell{background:radial-gradient(circle at 55% 50%,#2c5fb0 0%,#6fb2e0 30%,#bfe3f3 75%)}
.solution{position:absolute;top:388px;width:266px;text-align:center}
.solution h3{font-weight:700;font-size:15.5px;color:var(--blue);margin-bottom:8px}
.solution p{font-size:12.3px;line-height:17px;color:var(--ink)}

/* thanks */
.s-thanks{top:3173px;background:linear-gradient(180deg,#1b1b1b 0%,#101010 100%)}
.s-thanks .brand-block{position:absolute;left:0;right:0;top:170px;display:flex;flex-direction:column;align-items:center;gap:14px}
.s-thanks .brand-dot{width:96px;height:96px;background:var(--green)}
.s-thanks .brand-name{font-size:30px;color:var(--green)}
.s-thanks .thanks{position:absolute;top:360px;width:100%;text-align:center;font-family:"Lato",sans-serif;font-weight:400;font-size:40px;color:var(--white)}
</style>
</head>
<body>

<section class="slide s-welcome">
  <div class="bg" role="img" aria-label="Dark blue background photo of a DNA double helix"></div>
  <h1 class="title">WELCOME TO MEDORAVIX</h1>
  <p class="subtitle">Global Health Sciences</p>
  <div class="brand"><span class="brand-dot"></span><span class="brand-name">MedoraVix</span></div>
</section>

<section class="slide s-services">
  <div class="brand"><span class="brand-dot"></span><span class="brand-name">MedoraVix</span></div>
  <svg class="tab" viewBox="0 0 270 60" aria-hidden="true">
    <polygon points="0,0 30,0 48,60 18,60" fill="#46b21b"/>
    <polygon points="20,0 270,0 270,60 38,60" fill="#0f3a73"/>
  </svg>
  <div class="tab-label">OUR SERVICES</div>

  <div class="card" style="left:21px">
    <svg class="card-icon" viewBox="0 0 85 85" aria-hidden="true"><circle cx="42.5" cy="42.5" r="42.5" fill="#46b21b"/><path d="M24 56 C36 50 48 36 60 28 M26 60 C40 52 50 36 62 32" stroke="#fff" stroke-width="3.5" fill="none"/><path d="M32 50l8 6M40 44l8 6M48 37l7 6" stroke="#fff" stroke-width="3"/></svg>
    <h3>LOREM IPSUM</h3>
    <p>There are many variations of passages of Lorem Ipsum available, but the majority have suffered alteration in some form, by injected humour, or randomised words which don't look even slightly believable. f you are going to use a passage of Lorem Ipsum, you need to be sure there isn't anything embarrassing hidden in the middle of text. All the Lorem Ipsum generators.</p>
  </div>
  <div class="card" style="left:265px">
    <svg class="card-icon" viewBox="0 0 85 85" aria-hidden="true"><circle cx="42.5" cy="42.5" r="42.5" fill="#46b21b"/><path d="M42.5 20v26M42.5 46L26 60M42.5 46L59 60M33 34l9.5 12M52 34l-9.5 12" stroke="#fff" stroke-width="4" stroke-linecap="round" fill="none"/></svg>
    <h3>LOREM IPSUM</h3>
    <p>There are many variations of passages of Lorem Ipsum available, but the majority have suffered alteration in some form, by injected humour, or randomised words which don't look even slightly believable. f you are going to use a passage of Lorem Ipsum, you need to be sure there isn't anything embarrassing hidden in the middle of text. All the Lorem Ipsum generators.</p>
  </div>
  <div class="card" style="left:509px">
    <svg class="card-icon" viewBox="0 0 85 85" aria-hidden="true"><circle cx="42.5" cy="42.5" r="42.5" fill="#46b21b"/><rect x="33" y="18" width="19" height="46" rx="9" fill="none" stroke="#fff" stroke-width="3.5"/><line x1="30" y1="18" x2="55" y2="18" stroke="#fff" stroke-width="3.5"/><circle cx="42.5" cy="50" r="4" fill="#fff"/><line x1="33" y1="38" x2="52" y2="38" stroke="#fff" stroke-width="3"/></svg>
    <h3>LOREM IPSUM</h3>
    <p>There are many variations of passages of Lorem Ipsum available, but the majority have suffered alteration in some form, by injected humour, or randomised words which don't look even slightly believable. f you are going to use a passage of Lorem Ipsum, you need to be sure there isn't anything embarrassing hidden in the middle of text. All the Lorem Ipsum generators.</p>
  </div>
  <div class="card" style="left:756px">
    <svg class="card-icon" viewBox="0 0 85 85" aria-hidden="true"><circle cx="42.5" cy="42.5" r="42.5" fill="#46b21b"/><g fill="none" stroke="#fff" stroke-width="2.5"><polygon points="42.5,22 50,26.5 50,35 42.5,39.5 35,35 35,26.5"/><polygon points="35,35 42.5,39.5 42.5,48 35,52.5 27.5,48 27.5,39.5"/><polygon points="50,35 57.5,39.5 57.5,48 50,52.5 42.5,48 42.5,39.5"/><polygon points="42.5,48 50,52.5 50,61 42.5,65.5 35,61 35,52.5"/></g></svg>
    <h3>LOREM IPSUM</h3>
    <p>There are many variations of passages of Lorem Ipsum available, but the majority have suffered alteration in some form, by injected humour, or randomised words which don't look even slightly believable. f you are going to use a passage of Lorem Ipsum, you need to be sure there isn't anything embarrassing hidden in the middle of text. All the Lorem Ipsum generators.</p>
  </div>
  <div class="footer-bar green"></div><div class="footer-bar blue"></div>
</section>

<section class="slide s-about">
  <svg class="visual" viewBox="0 0 1002 563" aria-hidden="true">
    <defs>
      <radialGradient id="deepBlue" cx="65%" cy="45%" r="65%">
        <stop offset="0" stop-color="#2a6bb0"/><stop offset=".6" stop-color="#133e78"/><stop offset="1" stop-color="#0b2246"/>
      </radialGradient>
    </defs>
    <path d="M539 0 C420 130 400 420 525 563 L1002 563 L1002 0 Z" fill="#46b21b"/>
    <path d="M555 0 C440 130 420 420 545 563 L1002 563 L1002 0 Z" fill="url(#deepBlue)" role="img" aria-label="Photo of a glowing blue DNA helix"/>
  </svg>
  <div class="brand"><span class="brand-dot"></span><span class="brand-name">MedoraVix</span></div>
  <h2>ABOUT US</h2>
  <div class="copy">
    <p>There are many variations of passages of Lorem Ipsum available, but the majority have suffered alteration in some form, by injected humour, or randomised words which don't look even slightly believable. If you are going to use a passage of Lorem Ipsum, you need to be sure there isn't anything embarrassing hidden in the middle of text. All the Lorem Ipsum generators on the Internet tend to repeat predefined chunks as necessary, making this the first true generator on the Internet. It uses a dictionary of over 200 Latin words, combined with a handful of model sentence structures.</p>
    <p class="left">It is a long established fact that a reader will be distracted by the readable content of a page when looking at its layout. The point of using Lorem Ipsum is that it has a more-or-less normal distribution of letters, as opposed to using 'Content here, content here', making it look like readable English.</p>
    <p class="left">Sed ut perspiciatis unde omnis iste natus error sit voluptatem accusantium doloremque laudantium, totam rem aperiam, eaque ipsa quae ab illo inventore</p>
  </div>
  <div class="footer-bar green"></div>
</section>

<section class="slide s-process">
  <div class="bg" role="img" aria-label="Soft light background photo of glass molecule structures"></div>
  <div class="brand" style="left:14px;top:14px"><span class="brand-dot" style="width:34px;height:34px"></span><span class="brand-name" style="font-size:27px">MedoraVix</span></div>

  <div class="note" style="left:223px;top:70px"><h4>LOREM IPSUM</h4><p>There are many variations of passa ges of Lorem Ipsum available, but the majority have suffered alteration in some form, by injected humour, or randomised words which don't look even slightly believable.</p></div>
  <div class="note" style="left:560px;top:70px"><h4>LOREM IPSUM</h4><p>There are many variations of passa ges of Lorem Ipsum available, but the majority have suffered alteration in some form, by injected humour, or randomised words which don't look even slightly believable.</p></div>

  <div class="stem" style="left:302px;top:188px;height:60px"></div><div class="pin" style="left:300px;top:188px"></div>
  <div class="stem" style="left:638px;top:188px;height:60px"></div><div class="pin" style="left:636px;top:188px"></div>
  <div class="stem" style="left:129px;top:278px;height:70px"></div><div class="pin" style="left:127px;top:344px"></div>
  <div class="stem" style="left:466px;top:278px;height:70px"></div><div class="pin" style="left:464px;top:344px"></div>
  <div class="stem" style="left:805px;top:278px;height:70px"></div><div class="pin" style="left:803px;top:344px"></div>

  <div class="step" style="left:59px;top:139px"><div class="step-ring"></div><div class="step-face">1</div></div>
  <div class="step" style="left:230px;top:246px"><div class="step-ring"></div><div class="step-face">2</div></div>
  <div class="step" style="left:396px;top:139px"><div class="step-ring"></div><div class="step-face">3</div></div>
  <div class="step" style="left:565px;top:246px"><div class="step-ring"></div><div class="step-face">4</div></div>
  <div class="step" style="left:735px;top:139px"><div class="step-ring"></div><div class="step-face">5</div></div>

  <div class="note" style="left:49px;top:362px"><h4>LOREM IPSUM</h4><p>There are many variations of passa ges of Lorem Ipsum available, but the majority have suffered alteration in some form, by injected humour, or randomised words which don't look even slightly believable.</p></div>
  <div class="note" style="left:386px;top:362px"><h4>LOREM IPSUM</h4><p>There are many variations of passa ges of Lorem Ipsum available, but the majority have suffered alteration in some form, by injected humour, or randomised words which don't look even slightly believable.</p></div>
  <div class="note" style="left:725px;top:362px"><h4>LOREM IPSUM</h4><p>There are many variations of passa ges of Lorem Ipsum available, but the majority have suffered alteration in some form, by injected humour, or randomised words which don't look even slightly believable.</p></div>

  <div class="footer-bar green"></div><div class="footer-bar blue"></div>
</section>

<section class="slide s-solutions">
  <div class="brand" style="left:18px;top:18px"><span class="brand-dot" style="width:34px;height:34px"></span><span class="brand-name" style="font-size:27px">MedoraVix</span></div>
  <div class="head">
    <h2>SOLUTIONS</h2>
    <p>At vero eos et accusamus et iusto odio dignissimos ducimus qui blanditiis</p>
  </div>

  <div class="photo dna" style="left:37px" role="img" aria-label="Photo of a translucent DNA strand"></div>
  <div class="photo care" style="left:351px" role="img" aria-label="Photo of hands holding a red heart"></div>
  <div class="photo cell" style="left:675px" role="img" aria-label="Photo of blue cells under a microscope"></div>

  <div class="solution" style="left:29px"><h3>LOREM IPSUM</h3><p>At vero eos et accusamus et iusto odio dignissimos ducimus qui blanditiis praesentium voluptatum deleniti atque corrupti quos dolores et quas molestias excepturi sint occaecati cupiditate non provident, similique sunt in culpa qui officia deserunt.</p></div>
  <div class="solution" style="left:343px"><h3>LOREM IPSUM</h3><p>At vero eos et accusamus et iusto odio dignissimos ducimus qui blanditiis praesentium voluptatum deleniti atque corrupti quos dolores et quas molestias excepturi sint occaecati cupiditate non provident, similique sunt in culpa qui officia deserunt.</p></div>
  <div class="solution" style="left:672px"><h3>LOREM IPSUM</h3><p>At vero eos et accusamus et iusto odio dignissimos ducimus qui blanditiis praesentium voluptatum deleniti atque corrupti quos dolores et quas molestias excepturi sint occaecati cupiditate non provident, similique sunt in culpa qui officia deserunt.</p></div>

  <div class="footer-bar green"></div><div class="footer-bar blue"></div>
</section>

<section class="slide s-thanks">
  <div class="brand-block"><span class="brand-dot"></span><span class="brand-name">MedoraVix</span></div>
  <p class="thanks">THANK YOU</p>
</section>

</body>
</html>
```